Brightvale Apparatus Co. Ltd.
Creative Brief
Simple
Obinnaya Kelechukwu
Managing Director
Nigeria: # 42 Chief Adebanwo Street Off Ikemba Ave., Rumuokor Port Harcourt, Rivers State USA: PO Box 38192, Fort Worth, TX 76108
+ 234 80 31478265 (Nigeria)
+ 1 817 926 4158 (USA)
+ 1 817 362 8197 (USA)
sales@brightvaleplant.com
www.brightvaleplant.com
Use this address in the letter-head: 58 Kolawale Rd., Ejigbo, Lagos State (Nigeria) 14 Maplerun Dr., Fort Worth, TX 76119 (USA)

```html
<!DOCTYPE html>
<html lang="en">
<head>
<meta charset="utf-8">
<title>Brightvale Apparatus Co. Ltd. – Business Card</title>
<link rel="stylesheet" href="https://fonts.googleapis.com/css2?family=Roboto:wght@400;500;700;900&family=Roboto+Condensed:wght@700&display=swap">
<style>
  :root {
    --brand-red: #d7141c;
    --deep-red: #9e0f14;
    --ink: #1a1a1a;
    --grey: #6b6b6b;
    --paper: #ffffff;
    --backdrop: #e9e9e9;
  }
  * { box-sizing: border-box; margin: 0; padding: 0; }
  html, body { width: 1200px; height: 980px; overflow: hidden; }
  body {
    background: var(--backdrop);
    font-family: "Roboto", Arial, sans-serif;
    color: var(--ink);
    position: relative;
  }
  .card {
    position: absolute;
    left: 215px;
    width: 770px;
    height: 440px;
    background: var(--paper);
    border-radius: 22px;
    overflow: hidden;
    box-shadow: 0 6px 18px rgba(0,0,0,.12);
  }
  .card--front { top: 30px; }
  .card--back { top: 510px; }
  .card__art { position: absolute; inset: 0; width: 100%; height: 100%; }

  /* front */
  .brand {
    position: absolute;
    left: 48px;
    top: 48px;
    display: flex;
    align-items: center;
    gap: 14px;
  }
  .brand__dot {
    width: 46px; height: 46px;
    border-radius: 50%;
    background: var(--brand-red);
    flex: none;
  }
  .brand__name {
    font-family: "Roboto Condensed", "Arial Narrow", sans-serif;
    font-weight: 700;
    font-size: 27px;
    line-height: 1.05;
    color: var(--brand-red);
    text-transform: uppercase;
    width: 250px;
  }
  .tagline {
    position: absolute;
    left: 110px;
    top: 118px;
    font-size: 11px;
    font-weight: 500;
    letter-spacing: 1.4px;
    color: var(--ink);
    text-transform: uppercase;
  }
  .contact {
    position: absolute;
    left: 48px;
    top: 170px;
    list-style: none;
    font-size: 12.5px;
    line-height: 1.45;
    color: var(--ink);
  }
  .contact li {
    display: flex;
    align-items: flex-start;
    gap: 10px;
    margin-bottom: 7px;
  }
  .contact__icon {
    flex: none;
    width: 16px; height: 16px;
    margin-top: 1px;
  }
  .person {
    position: absolute;
    right: 48px;
    bottom: 38px;
    text-align: right;
  }
  .person__name {
    font-size: 21px;
    font-weight: 700;
    color: var(--deep-red);
  }
  .person__title {
    font-size: 14px;
    color: var(--ink);
    margin-top: 4px;
  }

  /* back */
  .back-brand {
    position: absolute;
    left: 0; right: 0;
    top: 150px;
    display: flex;
    justify-content: center;
    align-items: center;
    gap: 16px;
  }
  .back-brand .brand__dot { width: 70px; height: 70px; }
  .back-brand .brand__name { font-size: 34px; width: auto; }
  .back-brand__tm {
    font-size: 13px;
    font-weight: 700;
    color: var(--brand-red);
    align-self: flex-start;
  }
  .website {
    position: absolute;
    left: 0; right: 0;
    top: 268px;
    text-align: center;
    font-size: 19px;
    letter-spacing: 1px;
    color: var(--grey);
  }
  .website__name { color: var(--brand-red); font-weight: 700; }
</style>
</head>
<body>

<section class="card card--front" aria-label="Business card front">
  <svg class="card__art" viewBox="0 0 770 440" preserveAspectRatio="none" aria-hidden="true">
    <path d="M40 30 Q180 -6 330 20" fill="none" stroke="var(--brand-red)" stroke-width="5"/>
    <path d="M400 0 C520 50 660 170 770 330 L770 0 Z" fill="var(--ink)"/>
    <path d="M425 0 C540 50 680 160 770 300 L770 0 Z" fill="var(--brand-red)"/>
  </svg>

  <div class="brand">
    <span class="brand__dot"></span>
    <span class="brand__name">Brightvale Apparatus Co. Ltd.</span>
  </div>
  <p class="tagline">Sourcing · Sales · Service · Rental</p>

  <ul class="contact">
    <li>
      <svg class="contact__icon" viewBox="0 0 16 16"><path d="M8 1a5 5 0 0 0-5 5c0 4 5 9 5 9s5-5 5-9a5 5 0 0 0-5-5zm0 7a2 2 0 1 1 0-4 2 2 0 0 1 0 4z" fill="var(--brand-red)"/></svg>
      <span># 42 Chief Adebanwo Street Off Ikemba Ave., Rumuokor<br>Port Harcourt, Rivers State<br>PO Box 38192, Fort Worth, TX 76108</span>
    </li>
    <li>
      <svg class="contact__icon" viewBox="0 0 16 16"><path d="M4 1h3l1 4-2 1a9 9 0 0 0 4 4l1-2 4 1v3a2 2 0 0 1-2 2A12 12 0 0 1 2 3a2 2 0 0 1 2-2z" fill="var(--brand-red)"/></svg>
      <span>+ 234 80 31478265 (Nigeria)<br>+ 1 817 926 4158 (USA)<br>+ 1 817 362 8197 (USA)</span>
    </li>
    <li>
      <svg class="contact__icon" viewBox="0 0 16 16"><rect x="1" y="3" width="14" height="10" rx="1.5" fill="var(--brand-red)"/><path d="M1.5 4 8 9l6.5-5" fill="none" stroke="#fff" stroke-width="1.3"/></svg>
      <span>sales@brightvaleplant.com</span>
    </li>
    <li>
      <svg class="contact__icon" viewBox="0 0 16 16"><circle cx="8" cy="8" r="6.5" fill="none" stroke="var(--brand-red)" stroke-width="1.6"/><path d="M1.5 8h13M8 1.5c-3 3.5-3 9.5 0 13M8 1.5c3 3.5 3 9.5 0 13" fill="none" stroke="var(--brand-red)" stroke-width="1.2"/></svg>
      <span>www.brightvaleplant.com</span>
    </li>
  </ul>

  <div class="person">
    <p class="person__name">Obinnaya Kelechukwu</p>
    <p class="person__title">Managing Director</p>
  </div>
</section>

<section class="card card--back" aria-label="Business card back">
  <div class="back-brand">
    <span class="brand__dot"></span>
    <span class="brand__name">Brightvale Apparatus Co. Ltd.</span>
    <span class="back-brand__tm">TM</span>
  </div>
  <p class="website">www.<span class="website__name">brightvaleplant</span>.com</p>
</section>

</body>
</html>
```